Modern Billboard Ad for Criminal Defense Firm

10.5 x 36 We're looking for something to set us apart from the local competition. Looking for sleek and modern. We're a mid-sized firm in a small market city. We want to give the artist room to be creative on this one.
Thanks

Target Market(s)

Adult clients who have been charged with a crime/DWI

Industry/Entity Type

legal

Font styles to use
Serif
Sans Serif

Requirements
Must have
• Needs to have the firm name in large lettering. Law Offices of Marcus T Whitfield. “PLLC” does not have to be included. Phone number of (555) 384-1927 should be included but not the main focus.
Nice to have
• A call to action or something similar. “Don’t go it alone, call today.”, “ Arrested?”

```html
<!DOCTYPE html>
<html lang="en">
<head>
<meta charset="utf-8">
<title>Law Offices of Marcus T Whitfield — Billboard</title>
<link rel="stylesheet" href="https://fonts.googleapis.com/css2?family=Alfa+Slab+One&family=PT+Sans:wght@400&display=swap">
<style>
  :root {
    --page-bg: #e9ecef;
    --sky-blue: #18a9e0;
    --deep-blue: #15699c;
    --panel-black: #0b0d10;
    --title-white: #f4f2f3;
    --pill-white: #ecebee;
    --tagline-navy: #1c4f78;
    --photo-light: #b9b9b9;
    --photo-dark: #4a4a4a;
  }
  * { margin: 0; padding: 0; box-sizing: border-box; }
  html, body {
    width: 1200px; height: 900px; overflow: hidden;
    background: var(--page-bg);
  }
  .billboard {
    position: absolute;
    left: 40px; top: 310px;
    width: 1120px; height: 280px;
    overflow: hidden;
    background: radial-gradient(ellipse at 45% 55%, var(--sky-blue) 0%, #1a94cb 55%, var(--deep-blue) 100%);
  }
  .attorney-photo {
    position: absolute;
    left: 0; top: 22px;
    width: 236px; height: 258px;
    background: linear-gradient(160deg, var(--photo-light) 0%, #7d7d7d 55%, var(--photo-dark) 100%);
  }
  .name-panel {
    position: absolute;
    left: 248px; top: 0;
    width: 805px; height: 217px;
    background: var(--panel-black);
    border-radius: 0 0 60px 60px;
    display: flex; flex-direction: column;
    align-items: center; justify-content: center;
    padding-bottom: 8px;
  }
  .firm-name {
    font-family: "Alfa Slab One", "Rockwell", serif;
    font-weight: 400;
    color: var(--title-white);
    font-size: 74px;
    line-height: 0.98;
    letter-spacing: -1.5px;
    text-align: center;
    text-transform: lowercase;
  }
  .firm-name span { display: block; }
  .tagline-bar {
    position: absolute;
    left: 274px; top: 237px;
    width: 775px; height: 43px;
    background: var(--pill-white);
    border-radius: 24px 24px 0 0;
    display: flex; align-items: center; justify-content: center;
  }
  .tagline {
    font-family: "PT Sans", "Myriad Pro", sans-serif;
    font-size: 24px;
    color: var(--tagline-navy);
    white-space: nowrap;
  }
</style>
</head>
<body>
  <main class="billboard">
    <div class="attorney-photo" role="img" aria-label="Black and white portrait of the attorney in a vest and tie, jacket over his shoulder"></div>
    <div class="name-panel">
      <h1 class="firm-name"><span>law offices of</span><span>marcus t whitfield</span></h1>
    </div>
    <div class="tagline-bar">
      <p class="tagline">“Don’t go it alone, call today. Arrested?”(555) 384-1927</p>
    </div>
  </main>
</body>
</html>
```